Need a design for Loan Site with new age design

We need a design for our site www.fernpivot.in , we deal with different verticals like home loan, personal loan, loan against property and business loans. Feel free to get in touch if you have any questions.

I have like the concept of the drop down on the eye level where consumer is able to select the product they wish and continue with the form https://www.tallowcrest.com/ . They are in the same line of business as we are.

Here are few more designs which i personally like just to get idea about the taste

https://plumweatherly.com/
http://vexlar.com/partners

Industry/Entity Type

Loan

Number of Pages Required

2 page

Colors
34a7d7
add136
faa54b
fbee3e

Requirements
Must have
• I have like the concept of the drop down on the eye level where consumer is able to select the product they wish and continue with the form https://www.tallowcrest.com/ . They are in the same line of business as we are.
• Here are few more designs which i personally like just to get idea about the taste
• https://plumweatherly.com/
• http://vexlar.com/partners

```html
<!DOCTYPE html>
<html lang="en">
<head>
<meta charset="utf-8">
<title>Fern Pivot – Loans</title>
<link href="https://fonts.googleapis.com/css2?family=Open+Sans:wght@400;600;700&family=Archivo+Black&display=swap" rel="stylesheet">
<style>
  :root{
    --brand-blue:#34a7d7;
    --brand-green:#add136;
    --brand-orange:#faa54b;
    --brand-yellow:#fbee3e;
    --ink:#111111;
    --white:#ffffff;
    --hero-top:#4a3fb8;
    --hero-bottom:#2c6fd0;
    --navy:#0b2440;
    --footer:#000000;
  }
  *{box-sizing:border-box;margin:0;padding:0}
  html,body{width:1200px;height:2420px;overflow:hidden;background:var(--white)}
  body{position:relative;font-family:"Open Sans",Arial,sans-serif;color:var(--ink)}
  .abs{position:absolute}

  /* header */
  .site-header{left:0;top:0;width:1200px;height:88px;background:var(--white)}
  .brand{left:14px;top:18px;display:flex;align-items:center;gap:12px}
  .brand-mark{width:44px;height:44px;background:var(--brand-blue)}
  .brand-name{font-size:26px;font-weight:600;color:var(--brand-blue);white-space:nowrap}
  .main-nav{left:386px;top:16px;display:flex;gap:26px;font-size:30px;line-height:1.2;color:var(--ink);white-space:nowrap}
  .main-nav span{white-space:nowrap}
  .main-nav .active{border-bottom:3px solid var(--ink)}

  /* hero */
  .hero{left:0;top:88px;width:1200px;height:552px;
    background:linear-gradient(180deg,var(--hero-top),var(--hero-bottom) 70%,#3c8fe0)}
  .hero-title{left:0;top:172px;width:1200px;text-align:center;font-size:42px;font-weight:700;color:var(--brand-yellow);white-space:nowrap}
  .hero-sub{left:0;top:248px;width:1200px;text-align:center;font-size:22px;letter-spacing:4px;color:var(--white);white-space:nowrap}
  .loan-form{left:256px;top:344px;height:96px;display:flex;gap:16px}
  .select-box{width:256px;height:96px;background:var(--white);display:flex;align-items:center;justify-content:center;gap:22px;font-size:18px;white-space:nowrap}
  .select-box svg{width:30px;height:20px}
  .search-btn{width:168px;height:96px;background:var(--white);display:flex;align-items:center;justify-content:center;font-size:18px;font-weight:600}

  /* features */
  .features{left:0;top:640px;width:1200px;height:790px;background:var(--brand-green)}
  .features-title{left:0;top:52px;width:1200px;text-align:center;font-family:"Archivo Black",Arial,sans-serif;font-weight:400;font-size:84px;letter-spacing:2px}
  .features-rule{left:416px;top:162px;width:384px;height:8px;background:var(--ink)}
  .features-map{left:0;top:0}
  .feature{width:300px;text-align:center;font-size:20px;line-height:1.45}

  /* partners */
  .partners-heading{left:0;top:1508px;width:1200px;text-align:center;font-size:44px;font-weight:400;white-space:nowrap}
  .partner-badge{top:1632px;height:144px;background:#000;display:flex;align-items:center;justify-content:center}
  .partner-badge span{width:60%;height:24px;background:#2a2a2a;border-radius:4px}

  /* call to action */
  .cta{left:0;top:1820px;width:1200px;height:212px;background:var(--navy);overflow:hidden}
  .cta-art-left{left:-60px;top:-40px;width:220px;height:220px;border-radius:50%;background:radial-gradient(circle,#1d4d7a,#0b2440 70%)}
  .cta-art-right{left:740px;top:0;width:460px;height:212px;background:linear-gradient(90deg,rgba(11,36,64,0),#1f6fa8 40%,#f0a93d 85%,#d43b3b)}
  .cta-title{left:0;top:36px;width:1200px;text-align:center;font-size:36px;color:var(--white);white-space:nowrap}
  .cta-btn{left:510px;top:110px;width:180px;height:50px;background:var(--brand-orange);color:var(--white);font-size:22px;font-weight:600;display:flex;align-items:center;justify-content:center;white-space:nowrap}

  /* footer */
  .site-footer{left:0;top:2032px;width:1200px;height:388px;background:var(--footer);color:var(--white)}
  .footer-brand{left:60px;top:30px;font-size:32px;font-weight:700}
  .footer-links{left:60px;top:100px;list-style:none;font-size:22px;line-height:40px}
  .footer-divider{left:0;top:0}
  .social-title{left:792px;top:140px;font-size:38px;white-space:nowrap}
  .social-dot{top:212px;width:58px;height:58px;border-radius:50%}
</style>
</head>
<body>

<header class="site-header abs">
  <div class="brand abs"><span class="brand-mark"></span><span class="brand-name">Fern Pivot</span></div>
  <nav class="main-nav abs">
    <span class="active">Home</span><span>Who we are</span><span>Services</span><span>Blog</span><span>Career</span><span>Reachus</span>
  </nav>
</header>

<section class="hero abs" role="img" aria-label="City skyline of tall office towers in blue tones">
  <h1 class="hero-title abs">Looking For a Secured or Unsecured Loan?</h1>
  <p class="hero-sub abs">We Will help You Best Interest Rates</p>
  <div class="loan-form abs">
    <div class="select-box">I Would Like to
      <svg viewBox="0 0 30 20"><path d="M0 0h30L15 20z" fill="#111"/></svg></div>
    <div class="select-box">Select Product
      <svg viewBox="0 0 30 20"><path d="M0 0h30L15 20z" fill="#111"/></svg></div>
    <div class="search-btn">Search</div>
  </div>
</section>

<section class="features abs">
  <h2 class="features-title abs">FEATURES</h2>
  <div class="features-rule abs"></div>
  <svg class="features-map abs" width="1200" height="790" viewBox="0 0 1200 790" fill="none" stroke="#111" stroke-width="2">
    <line x1="600" y1="200" x2="600" y2="760"/>
    <line x1="320" y1="344" x2="600" y2="344"/>
    <line x1="600" y1="464" x2="900" y2="464"/>
    <line x1="320" y1="600" x2="600" y2="600"/>
    <line x1="600" y1="732" x2="900" y2="732"/>
    <circle cx="452" cy="240" r="12"/><path d="M452 234v12M446 240h12"/>
    <path d="M736 388l22-10-8 22-4-8z"/>
    <rect x="440" y="468" width="18" height="24"/><rect x="446" y="462" width="18" height="24"/>
    <path d="M740 660l12-8 4 4-12 12-6 2z"/>
  </svg>
  <div class="feature abs" style="left:302px;top:272px">Get Approval<br>Within 7 Business Days</div>
  <div class="feature abs" style="left:602px;top:420px">Doorstep Deliveries</div>
  <div class="feature abs" style="left:302px;top:520px">Compare Quote from all<br>Major Institutions.</div>
  <div class="feature abs" style="left:602px;top:688px">Easy Documentation</div>
</section>

<h2 class="partners-heading abs">we work with all premium finacial institutions</h2>
<div class="partner-badge abs" style="left:16px;width:272px"><span></span></div>
<div class="partner-badge abs" style="left:328px;width:252px"><span></span></div>
<div class="partner-badge abs" style="left:632px;width:252px"><span></span></div>
<div class="partner-badge abs" style="left:928px;width:256px"><span></span></div>

<section class="cta abs">
  <div class="cta-art-left abs" role="img" aria-label="Decorative soft blue circles"></div>
  <div class="cta-art-right abs" role="img" aria-label="Illustration of a mobile phone, envelope and screens"></div>
  <p class="cta-title abs">What Are You Waiting For?</p>
  <div class="cta-btn abs">Inquire Now</div>
</section>

<footer class="site-footer abs">
  <div class="footer-brand abs">FERNPIVOT</div>
  <ul class="footer-links abs">
    <li>Home</li><li>Who we are</li><li>Services</li><li>Blog</li><li>Career</li><li>Reach us</li>
  </ul>
  <svg class="footer-divider abs" width="1200" height="388" viewBox="0 0 1200 388">
    <line x1="820" y1="28" x2="700" y2="368" stroke="#fff" stroke-width="4"/>
  </svg>
  <p class="social-title abs">Follow us on Social :</p>
  <span class="social-dot abs" style="left:804px;background:#2f5ba8"></span>
  <span class="social-dot abs" style="left:888px;background:#d8262b"></span>
  <span class="social-dot abs" style="left:972px;background:#3c7dc8"></span>
  <span class="social-dot abs" style="left:1056px;background:#c9222a"></span>
</footer>

</body>
</html>
```